HomeBridle business card and stationary design

We are looking for a simple yet elegant design for our mortgage company business card and stationary.

The card should include:
Name (Derek Walsh)
Title (CEO)
Phone Number (614-208-3917)
Address (48 Birchfield Court, Suite 314, Marlow, OH 43952)
Email (email@homebridle-example.com)
"NMLS" i.e. (NMLS 61947)
"Company NMLS" (Company NMLS 472815)

See above

```html
<!DOCTYPE html>
<html lang="en">
<head>
<meta charset="utf-8">
<title>HomeBridle Business Card</title>
<link href="https://fonts.googleapis.com/css2?family=Montserrat:wght@400;500;600;700&display=swap" rel="stylesheet">
<style>
  :root {
    --stage: #2a2b2d;
    --card: #1d1e20;
    --accent: #1ea4e0;
    --text: #f2f2f2;
    --muted: #b9bcc0;
    --emboss: #8e9196;
  }
  * { box-sizing: border-box; margin: 0; padding: 0; }
  html, body { width: 1200px; height: 900px; overflow: hidden; }
  body {
    background: var(--stage);
    font-family: "Montserrat", sans-serif;
    color: var(--text);
    display: flex;
    flex-direction: column;
    align-items: center;
    justify-content: center;
    gap: 36px;
  }
  .card {
    position: relative;
    width: 700px;
    height: 400px;
    background: var(--card);
    border-bottom: 8px solid var(--accent);
    box-shadow: 0 10px 30px rgba(0,0,0,.45);
  }

  /* Front */
  .card-front .person { position: absolute; left: 48px; top: 52px; }
  .person-name {
    color: var(--accent);
    font-weight: 700;
    font-size: 26px;
    letter-spacing: .5px;
    text-transform: uppercase;
  }
  .person-title { font-size: 16px; font-weight: 400; margin-top: 2px; }
  .divider {
    position: absolute;
    left: 48px; right: 48px; top: 132px;
    height: 1px;
    background: var(--accent);
  }
  .contact-list {
    position: absolute;
    left: 48px; top: 160px;
    list-style: none;
    font-size: 17px;
    line-height: 30px;
  }
  .contact-list li { display: flex; align-items: center; gap: 12px; }
  .contact-list svg { width: 15px; height: 15px; fill: var(--accent); flex: none; }
  .brand-name {
    position: absolute;
    right: 48px; top: 54px;
    font-size: 44px;
    font-weight: 600;
    color: var(--text);
    letter-spacing: .5px;
  }
  .address {
    position: absolute;
    right: 48px; bottom: 40px;
    text-align: right;
    font-size: 17px;
    line-height: 26px;
  }

  /* Back */
  .card-back .brand-name-large {
    position: absolute;
    left: 0; right: 0; top: 120px;
    text-align: center;
    font-size: 72px;
    font-weight: 600;
    color: var(--emboss);
    letter-spacing: 1px;
  }
  .license {
    position: absolute;
    left: 0; right: 0; bottom: 46px;
    text-align: center;
    font-size: 16px;
    letter-spacing: .5px;
  }
  .license .dot { color: var(--accent); margin: 0 10px; }
</style>
</head>
<body>

<section class="card card-front" aria-label="Business card front">
  <div class="person">
    <p class="person-name">Derek Walsh</p>
    <p class="person-title">CEO</p>
  </div>
  <p class="brand-name">HomeBridle</p>
  <div class="divider"></div>
  <ul class="contact-list">
    <li>
      <svg viewBox="0 0 24 24" aria-hidden="true"><path d="M6.6 10.8a15.1 15.1 0 0 0 6.6 6.6l2.2-2.2a1 1 0 0 1 1-.25 11.4 11.4 0 0 0 3.6.57 1 1 0 0 1 1 1V20a1 1 0 0 1-1 1A17 17 0 0 1 3 4a1 1 0 0 1 1-1h3.5a1 1 0 0 1 1 1c0 1.25.2 2.45.57 3.57a1 1 0 0 1-.25 1z"/></svg>
      614-208-3917
    </li>
    <li>
      <svg viewBox="0 0 24 24" aria-hidden="true"><path d="M2 5h20v14H2z M3 6l9 7 9-7" stroke="#1d1e20" stroke-width="1.5"/></svg>
      email@homebridle-example.com
    </li>
    <li>
      <svg viewBox="0 0 24 24" aria-hidden="true"><circle cx="12" cy="12" r="10"/><path d="M2 12h20M12 2c3 3 3 17 0 20M12 2c-3 3-3 17 0 20" stroke="#1d1e20" stroke-width="1.5" fill="none"/></svg>
      www.homebridle.com
    </li>
  </ul>
  <p class="address">48 Birchfield Court, Suite 314<br>Marlow, OH 43952</p>
</section>

<section class="card card-back" aria-label="Business card back">
  <p class="brand-name-large">HomeBridle</p>
  <p class="license">NMLS 61947<span class="dot">&#9679;</span>Company NMLS 472815</p>
</section>

</body>
</html>
```